Business Card for TQM

We need a Corporate style business card for a new Industrial recycling company based in Australia. We recycle industrial products from Mining companies, power stations and other large industry all around the country.

We want the card to represent a modern, innovative professional company that is an industry leader.

We want the card to be double sided. I think with the logo centred by itself on one side and the text displayed with all our details on the other side.

(or you could put the persons name with the job title on the side with the logo?? I'll leave that up to your creative sides)

Open to how you divide and place the information on the one side of the card.

I think the persons name and the title should have its own place. The rest of the information can be placed as you think is best and then I will provide feedback as to what I think works best.

I have attached the logo file so you can add that to the one side. Whether you use it in a smaller form on the second side too is an option but I'll leave that up to you initially?

Information required on the card is as follows

Darren Pollock
Director

0428 917 306

darren@tqmv.com.au

Po Box 582
Brindle ACT 2611

www.tqmv.com.au

ACN 273 581 926 (This can be in very small print and can be in the bottom corner of the card or somewhere not very prominent
Updates

Wanted to thank everyone for their submissions. 

We were really torn on about 5 designs in the end.

We decided to go with the first one we liked.

We have another company that is going to need logo and business card design in the coming weeks.

I will save your designer ID's so I can invite you all to that project. too!

Thanks again and all the best

Darren

Target Market(s)

Corporate and medium to large business clients

Industry/Entity Type

Industrial

```html
<!DOCTYPE html>
<html lang="en">
<head>
<meta charset="utf-8">
<title>TQM Business Card</title>
<link rel="stylesheet" href="https://fonts.googleapis.com/css2?family=Source+Sans+3:wght@400;700&display=swap">
<style>
  :root {
    --page: #ffffff;
    --card-white: #ffffff;
    --blue-top: #2b97c9;
    --blue-mid: #27799e;
    --blue-bottom: #24566c;
    --green: #69ae47;
    --ink-light: #ffffff;
    --ink-dark: #333638;
    --divider: #b9c3c8;
  }
  html, body {
    margin: 0;
    padding: 0;
    width: 1200px;
    height: 1000px;
    overflow: hidden;
    background: var(--page);
    font-family: "Source Sans 3", sans-serif;
  }
  .card {
    position: absolute;
    left: 184px;
    top: 238px;
    width: 832px;
    height: 524px;
    display: flex;
    box-shadow: 0 1px 5px rgba(0, 0, 0, 0.28);
  }
  .card__brand {
    width: 414px;
    height: 100%;
    background: var(--card-white);
    border-right: 2px solid var(--divider);
    display: flex;
    align-items: center;
    justify-content: center;
    gap: 18px;
  }
  .brand__dot {
    width: 56px;
    height: 56px;
    border-radius: 50%;
    background: var(--green);
  }
  .brand__name {
    font-size: 72px;
    font-weight: 700;
    color: var(--ink-dark);
    letter-spacing: 2px;
    line-height: 1;
  }
  .card__details {
    position: relative;
    flex: 1;
    height: 100%;
    background: linear-gradient(to bottom, var(--blue-top) 0%, var(--blue-mid) 50%, var(--blue-bottom) 100%);
    color: var(--ink-light);
  }
  .details__band {
    position: absolute;
    left: 0;
    right: 0;
    top: 109px;
    height: 113px;
    background: var(--green);
    padding-left: 82px;
    box-sizing: border-box;
  }
  .details__name {
    margin: 10px 0 0;
    font-size: 51px;
    font-weight: 400;
    line-height: 1.05;
    letter-spacing: 0.5px;
  }
  .details__title {
    margin: 0;
    font-size: 36px;
    font-weight: 400;
    line-height: 1.1;
  }
  .details__contact {
    position: absolute;
    left: 82px;
    top: 256px;
    margin: 0;
    padding: 0;
    list-style: none;
    font-size: 30px;
    line-height: 1;
  }
  .details__contact li {
    margin-bottom: 24px;
    letter-spacing: 0.5px;
  }
  .details__contact .details__address {
    line-height: 32px;
    margin-top: -4px;
    margin-bottom: 20px;
  }
  .details__acn {
    position: absolute;
    right: 20px;
    bottom: 12px;
    margin: 0;
    font-size: 14px;
    letter-spacing: 0.5px;
    opacity: 0.85;
  }
</style>
</head>
<body>
  <section class="card">
    <div class="card__brand">
      <span class="brand__dot"></span>
      <span class="brand__name">TQM</span>
    </div>
    <div class="card__details">
      <div class="details__band">
        <h1 class="details__name">Darren Pollock</h1>
        <p class="details__title">Director</p>
      </div>
      <ul class="details__contact">
        <li>0428 917 306</li>
        <li>darren@tqmv.com.au</li>
        <li class="details__address">Po Box 582<br>Brindle ACT 2611</li>
        <li>www.tqmv.com.au</li>
      </ul>
      <p class="details__acn">ACN 273 581 926</p>
    </div>
  </section>
</body>
</html>
```